Banner for a program to be used as a cover photo for Facebook

Banner design for a program I run called: The Craft of Swift Bloom
This is a 90 day implementation program for business owners who set one main goal to reach during that time. The focus of the program is to help them set the goal, create the strategy to reach the goal and take keystone actions to achieve the goal. This program (I run multiple at a time) is exclusive to only 8 people at a time...the price point of the program is $6,000.

Company Name: Woven Horizon

My title: Business Acceleration Mentor (BAM!)

My area of expertise: Helping business owners who already know what they do, who they serve, and have momentum (and sales) accelerate the growth of their business by eliminate what they don't need and simplifying the strategy to achieve mind blowing results. (Success habits, behaviors, routines, attitudes, speed of implementation, simplification, essentialism, focus, goal setting, high performance)

Who I want to attract: People who have made $25k - $75k in the last 12 months of their business (service based) who are action takers, big thinkers, in it to win it, take action even in the face of fear, committed, decision makers

Target Market(s)

Women business owners who have been in business for 2 - 5 years making at least $25k - $75k in their previous 12 months. They are feminine, married, moms, higher end and looking for a more exclusive and selective group of like-minded people to grow with. They are attracted to a more glamorous, boutique feel and desire to catapult the results in their business.

Industry/Entity Type

Business

Font styles to use
Sans Serif

Requirements
Must have
• Crisp, Clean, High End, Simple, Elegant, Picture of me
• Text on Banner:
• The Craft of Swift Bloom
• with Clara Westby, Business Acceleration Mentor
Should not have
• Men in suits in pictures.
• Corporate Feel.

```html
<!DOCTYPE html>
<html lang="en">
<head>
<meta charset="utf-8">
<title>The Craft of Swift Bloom — Cover Banner</title>
<link rel="stylesheet" href="https://fonts.googleapis.com/css2?family=Open+Sans:wght@600;700;800&display=swap">
<style>
  :root {
    --sky-top: #0b2443;
    --sky-mid: #3d6c96;
    --sky-low: #7ea3c2;
    --sky-glow: #dbe8f1;
    --crowd: #06090d;
    --text-white: #ffffff;
    --title-shade: #e2e6ea;
    --presenter: #dfe6ee;
    --shadow: rgba(0, 0, 0, 0.55);
    --portrait-light: #9fb8cc;
    --portrait-dark: #2d4a66;
  }
  html, body {
    margin: 0;
    padding: 0;
    width: 1200px;
    height: 444px;
    overflow: hidden;
    background: var(--sky-top);
  }
  .cover-banner {
    position: relative;
    width: 1200px;
    height: 444px;
    overflow: hidden;
    font-family: "Open Sans", Arial, sans-serif;
  }
  .hero-photo {
    position: absolute;
    inset: 0;
    background:
      radial-gradient(ellipse 330px 230px at 560px 360px, var(--sky-glow) 0%, rgba(219,232,241,0.45) 40%, rgba(219,232,241,0) 100%),
      linear-gradient(to bottom, var(--sky-top) 0%, var(--sky-mid) 45%, var(--sky-low) 70%, #4a5f72 80%, var(--crowd) 90%, var(--crowd) 100%);
  }
  .presenter-line {
    position: absolute;
    left: 48px;
    top: 52px;
    margin: 0;
    font-weight: 800;
    font-size: 24px;
    line-height: 1;
    letter-spacing: 0.2px;
    text-transform: uppercase;
    color: var(--presenter);
    text-shadow: 0 2px 3px var(--shadow);
  }
  .program-title {
    position: absolute;
    left: 46px;
    top: 78px;
    margin: 0;
    font-weight: 800;
    font-size: 74px;
    line-height: 1;
    letter-spacing: 0.3px;
    text-transform: uppercase;
    white-space: nowrap;
    background: linear-gradient(to bottom, var(--text-white) 35%, var(--title-shade) 100%);
    -webkit-background-clip: text;
    background-clip: text;
    color: transparent;
    filter: drop-shadow(0 3px 4px var(--shadow));
  }
  .mentor-line {
    position: absolute;
    left: 50px;
    top: 168px;
    margin: 0;
    font-weight: 600;
    font-size: 22px;
    line-height: 1;
    color: var(--text-white);
    text-shadow: 0 2px 3px var(--shadow);
  }
  .mentor-line strong {
    font-weight: 700;
  }
  .mentor-portrait {
    position: absolute;
    right: 48px;
    top: 160px;
    width: 120px;
    height: 120px;
    border-radius: 50%;
    border: 3px solid var(--text-white);
    background: radial-gradient(circle at 50% 40%, var(--portrait-light) 0%, var(--portrait-dark) 100%);
    box-shadow: 0 3px 8px var(--shadow);
  }
</style>
</head>
<body>
  <div class="cover-banner">
    <div class="hero-photo" role="img" aria-label="Photo: silhouettes of a group of people raising their fists in celebration on a hilltop against a glowing blue evening sky"></div>
    <p class="presenter-line">Woven Horizon Presents</p>
    <h1 class="program-title">The Craft of Swift Bloom</h1>
    <p class="mentor-line">with <strong>Clara Westby</strong>, Business Acceleration Mentor</p>
    <div class="mentor-portrait" role="img" aria-label="Portrait photo of Clara Westby"></div>
  </div>
</body>
</html>
```